Word Bureau Ostrelle Templates

We run a large number of businesses, including schools, airports, hotels and offices. We write reports on a daily basis and are looking for a strong and sexy WORD Template. We already have a logo in place (see graphical chart attached), that is rights' protected. We are looking for a beautiful wich reflect modern design and human aspects. Our logo has 2 design, full fill and watermark. It can be used in red or black.

Architects, Fire brigade, Building investors, contactors

• Arial, Calibri, ...

• Cover page, summary, Bullet points, Tables, Figures, Annex

```html
<!DOCTYPE html>
<html lang="en">
<head>
<meta charset="utf-8">
<title>Bureau Ostrelle – Report Template</title>
<link rel="stylesheet" href="https://fonts.googleapis.com/css2?family=Montserrat:wght@500&family=Open+Sans:wght@400;500;600;700&family=Roboto+Condensed:wght@400;700&display=swap">
<style>
  :root{
    --red:#e3302b;
    --ink:#1d1d1d;
    --grey-box:#ebebeb;
    --canvas:#e4e4e4;
    --label:#1e3a56;
    --white:#ffffff;
    --body:#2a2a2a;
  }
  *{box-sizing:border-box;margin:0;padding:0}
  html,body{width:1200px;height:866px;overflow:hidden;background:var(--canvas)}
  body{position:relative;font-family:"Open Sans",Arial,sans-serif;color:var(--ink)}
  .page{position:absolute;top:24px;width:533px;height:752px;background:var(--white);overflow:hidden;
        box-shadow:0 14px 18px -10px rgba(0,0,0,.35)}
  .page--cover{left:35px}
  .page--inner{left:634px}
  .page__art{position:absolute;inset:0;width:100%;height:100%}
  .page-label{position:absolute;top:798px;width:300px;margin-left:-150px;text-align:center;
        font-family:"Montserrat",Arial,sans-serif;font-weight:500;font-size:26px;letter-spacing:1px;color:var(--label)}
  .page-label--one{left:328px}
  .page-label--two{left:899px}

  /* cover */
  .brand{position:absolute;left:14px;top:40px;display:flex;align-items:flex-start;gap:14px}
  .brand__dot{width:34px;height:34px;border-radius:50%;background:var(--white);margin-top:8px}
  .brand__name{font-family:"Open Sans",Arial,sans-serif;font-weight:500;font-size:26px;line-height:28px;color:var(--white)}
  .cover-title{position:absolute;left:31px;top:488px;font-family:"Roboto Condensed",Arial Narrow,sans-serif;
        font-weight:700;font-size:57px;line-height:62px;color:var(--ink);letter-spacing:-.3px}
  .cover-title .accent{color:var(--red)}

  /* inner */
  .heading-one{position:absolute;left:22px;top:224px;font-family:"Roboto Condensed",Arial Narrow,sans-serif;
        font-weight:400;font-size:33px;line-height:1;color:var(--ink)}
  .heading-one .accent{color:var(--red)}
  .intro{position:absolute;left:24px;top:266px;width:486px;font-size:7.9px;line-height:11.8px;text-align:justify;color:var(--body)}
  .stat{position:absolute;text-align:center;color:var(--ink)}
  .stat__num{font-weight:700;font-size:27px;line-height:30px}
  .stat__text{font-size:7.8px;margin-top:6px}
  .stat--1{left:24px;width:145px;top:426px}
  .stat--2{left:181px;width:172px;top:426px;color:var(--white)}
  .stat--3{left:365px;width:145px;top:426px}
  .section-title{font-weight:700;font-size:10.5px;line-height:12px;color:var(--ink)}
  .section-title .accent{color:var(--red)}
  .col{position:absolute;top:556px}
  .col--left{left:24px;width:250px}
  .col--right{left:310px;width:200px}
  .bullets{list-style:none;margin-top:13px}
  .bullets li{position:relative;padding-left:10px;font-size:7.8px;line-height:10px;height:23.2px}
  .bullets li::before{content:"";position:absolute;left:0;top:3px;width:4px;height:4px;border-radius:50%;background:var(--red)}
  .col p{font-size:7.8px;line-height:11.6px;text-align:justify;color:var(--body);margin-top:8px}
  .col .section-title + p{margin-bottom:14px}
  .footer{position:absolute;left:0;right:0;top:714px;height:38px;display:flex;align-items:center;
        padding:0 23px;color:var(--white);font-size:7.5px}
  .footer__web{flex:1}
  .footer__brand{position:absolute;left:236px;top:9px;display:flex;align-items:center;gap:5px;
        font-weight:500;font-size:9.5px;line-height:10px}
  .footer__brand .dot{width:12px;height:12px;border-radius:50%;background:var(--white)}
</style>
</head>
<body>

<section class="page page--cover">
  <svg class="page__art" viewBox="0 0 666 940" preserveAspectRatio="none">
    <path d="M0,0 L345,0 C300,100 290,180 270,200 L0,285 Z" fill="var(--red)"/>
    <path role="img" aria-label="Photo: palace-like building lit at night behind palm trees and a waterfront"
          d="M390,0 L666,0 L666,718 C470,650 360,520 345,380 C335,250 345,100 390,0 Z" fill="url(#nightScene)"/>
    <defs>
      <linearGradient id="nightScene" x1="0" y1="0" x2="0" y2="1">
        <stop offset="0" stop-color="#1d2550"/>
        <stop offset=".3" stop-color="#c9a971"/>
        <stop offset=".6" stop-color="#3b4a2a"/>
        <stop offset="1" stop-color="#2a2218"/>
      </linearGradient>
      <linearGradient id="workerScene" x1="0" y1="0" x2="1" y2="1">
        <stop offset="0" stop-color="#c7c3b8"/>
        <stop offset="1" stop-color="#5e564c"/>
      </linearGradient>
      <linearGradient id="deskScene" x1="0" y1="0" x2="1" y2="1">
        <stop offset="0" stop-color="#2c4a6e"/>
        <stop offset=".55" stop-color="#c7b49a"/>
        <stop offset="1" stop-color="#e7e4de"/>
      </linearGradient>
    </defs>
    <path d="M365,-10 C320,100 310,250 320,380 C340,520 450,670 680,740" fill="none" stroke="var(--ink)" stroke-width="45"/>
    <path d="M-10,318 Q100,270 200,232" fill="none" stroke="var(--ink)" stroke-width="45"/>
    <circle cx="272" cy="292" r="126" fill="var(--white)"/>
    <circle role="img" aria-label="Photo: man working on a laptop seated by a window" cx="272" cy="292" r="117" fill="url(#workerScene)"/>
    <circle cx="366" cy="545" r="48" fill="var(--red)"/>
    <circle cx="567" cy="692" r="29" fill="var(--white)"/>
    <circle cx="567" cy="692" r="24" fill="var(--red)"/>
    <g fill="none" stroke="var(--red)" stroke-width="2.6" stroke-linejoin="round">
      <polygon transform="translate(49,572)" points="0,-17 5,-6 17,-5 8,3 11,15 0,9 -11,15 -8,3 -17,-5 -5,-6"/>
      <polygon transform="translate(102,572)" points="0,-17 5,-6 17,-5 8,3 11,15 0,9 -11,15 -8,3 -17,-5 -5,-6"/>
      <polygon transform="translate(154,572)" points="0,-17 5,-6 17,-5 8,3 11,15 0,9 -11,15 -8,3 -17,-5 -5,-6"/>
      <polygon transform="translate(207,572)" points="0,-17 5,-6 17,-5 8,3 11,15 0,9 -11,15 -8,3 -17,-5 -5,-6"/>
      <polygon transform="translate(259,572)" points="0,-17 5,-6 17,-5 8,3 11,15 0,9 -11,15 -8,3 -17,-5 -5,-6"/>
    </g>
    <rect x="31" y="855" width="139" height="7" fill="var(--red)"/>
    <rect x="0" y="905" width="666" height="4" fill="var(--red)"/>
    <rect x="0" y="912" width="666" height="28" fill="var(--ink)"/>
  </svg>
  <div class="brand">
    <span class="brand__dot"></span>
    <span class="brand__name">Bureau<br>Ostrelle</span>
  </div>
  <h1 class="cover-title">Welcome to<br><span class="accent">Lorem Ipsum</span> Text<br>Goes Here</h1>
</section>

<section class="page page--inner">
  <svg class="page__art" viewBox="0 0 666 940" preserveAspectRatio="none">
    <path role="img" aria-label="Photo: architects' desk with drawings, pencils and a mug"
          d="M0,0 H666 V45 C560,130 420,185 300,193 C180,200 80,192 0,168 Z" fill="url(#deskScene)"/>
    <path d="M0,195 C120,215 200,220 300,212 C450,200 570,140 666,70 V98 C560,175 440,235 300,243 C180,250 80,248 0,243 Z" fill="var(--ink)"/>
    <circle cx="303" cy="215" r="36" fill="var(--white)"/>
    <circle cx="303" cy="215" r="31" fill="var(--red)"/>
    <circle cx="567" cy="125" r="26" fill="var(--white)"/>
    <circle cx="567" cy="125" r="22" fill="var(--red)"/>
    <rect x="30" y="449" width="181" height="180" fill="var(--grey-box)"/>
    <rect x="226" y="432" width="215" height="215" fill="var(--red)"/>
    <rect x="456" y="449" width="181" height="180" fill="var(--grey-box)"/>
    <!-- briefcase -->
    <g transform="translate(120,500)" fill="var(--ink)">
      <rect x="-18" y="-12" width="36" height="24" rx="2"/>
      <rect x="-7" y="-19" width="14" height="8" fill="none" stroke="var(--ink)" stroke-width="3"/>
      <rect x="-15" y="-3" width="30" height="2" fill="var(--grey-box)"/>
      <path d="M0,2 L4,10 L0,20 L-4,10 Z"/>
    </g>
    <!-- monitor -->
    <g transform="translate(333,500)" fill="var(--white)">
      <rect x="-22" y="-20" width="44" height="32" rx="2"/>
      <rect x="-18" y="-16" width="36" height="24" fill="var(--red)"/>
      <rect x="-8" y="-14" width="16" height="20"/>
      <rect x="-3" y="12" width="6" height="6"/>
      <rect x="-11" y="18" width="22" height="3"/>
    </g>
    <!-- buildings -->
    <g transform="translate(547,500)" fill="var(--ink)">
      <rect x="-20" y="-20" width="18" height="42"/>
      <rect x="-2" y="-6" width="22" height="28"/>
      <g fill="var(--grey-box)">
        <rect x="-16" y="-14" width="4" height="4"/><rect x="-9" y="-14" width="4" height="4"/>
        <rect x="-16" y="-5" width="4" height="4"/><rect x="-9" y="-5" width="4" height="4"/>
        <rect x="-16" y="4" width="4" height="4"/><rect x="3" y="2" width="4" height="4"/>
        <rect x="11" y="2" width="4" height="4"/><rect x="3" y="11" width="12" height="3"/>
      </g>
    </g>
    <rect x="0" y="884" width="666" height="4" fill="var(--red)"/>
    <rect x="0" y="892" width="666" height="48" fill="var(--ink)"/>
  </svg>

  <h2 class="heading-one"><span class="accent">Heading</span> One</h2>
  <p class="intro">Lorem Ipsum is simply dummy text of the printing and typesetting industry. Lorem Ipsum has been the industry's standard dummy text ever since the 1500s, when an unknown printer took a galley of type and scrambled it to make a type specimen book. It has survived not only five centuries, but also the leap into electronic typesetting, remaining essentially unchanged. It was popularised in the 1960s with the release of Letraset sheets containing Lorem Ipsum passages.</p>

  <div class="stat stat--1"><div class="stat__num">301</div><div class="stat__text">Lorem Ipsum is simply dummy text.</div></div>
  <div class="stat stat--2"><div class="stat__num">500</div><div class="stat__text">Lorem Ipsum is simply dummy text.</div></div>
  <div class="stat stat--3"><div class="stat__num">201</div><div class="stat__text">Lorem Ipsum is simply dummy text.</div></div>

  <div class="col col--left">
    <h3 class="section-title">TITLE <span class="accent">GOES HERE</span></h3>
    <ul class="bullets">
      <li>Lorem Ipsum is simply dummy text of the printing.</li>
      <li>Lorem Ipsum is simply dummy text of the printing.</li>
      <li>Lorem Ipsum is simply dummy text of the printing.</li>
      <li>Lorem Ipsum is simply dummy text of the printing.</li>
    </ul>
  </div>
  <div class="col col--right">
    <h3 class="section-title">TITLE <span class="accent">GOES HERE</span></h3>
    <p>Lorem Ipsum is simply dummy text of the printing and typesetting industry. Lorem Ipsum has been the industry's standard dummy text ever since the 1500s.</p>
    <h3 class="section-title">TITLE <span class="accent">GOES HERE</span></h3>
    <p>Lorem Ipsum is simply dummy text of the printing and typesetting industry.</p>
  </div>

  <footer class="footer">
    <span class="footer__web">www.ostrelle-reports.com</span>
    <span class="footer__brand"><span class="dot"></span><span>Bureau<br>Ostrelle</span></span>
    <span class="footer__num">2</span>
  </footer>
</section>

<div class="page-label page-label--one">PAGE - 01</div>
<div class="page-label page-label--two">PAGE - 02</div>

</body>
</html>
```